Big Room Track needs a CD cover!

I need a CD cover for a Big Room track which will be released soon. Please orientate at the cover of any existing track. It would be good to find a design which fits this. Its planned to generate a child of corporate design for upcoming releases. Please find a demo of the track and my logo to use in the cover. The name of the track is not found yet. Please use a short demo text to show where the title could be so I can add it afterwards.

Target Market(s)

Music streaming services. EDM Scene. Festival. Promotion.

Colors

Designer to choose colors to be used in the design.

Requirements
Must have
• Needs to be kind of a corporate design with the existing cover of another released track of mine. (Not the exact picture but use of logo and track title in this font). Needs to match the feel of the track (demo provided).
Nice to have
• Should reflect the energy of the track. Light colors are appreciated.
Should not have
• No kiddy pictures (like comic or something).

```html
<!DOCTYPE html>
<html lang="en">
<head>
<meta charset="UTF-8">
<title>Big Room Track – Cover</title>
<link href="https://fonts.googleapis.com/css2?family=Arimo:wght@400;700&display=swap" rel="stylesheet">
<style>
  :root {
    --stage: #565958;
    --deep-navy: #1a1640;
    --electric-blue: #2fa8f0;
    --ice: #d9f3ff;
    --violet: #5a3fa8;
    --magenta: #c02a86;
    --plum: #3a1f6e;
    --title-ink: #0d0d14;
    --brand-ink: #ffffff;
  }
  html, body {
    margin: 0;
    width: 1200px;
    height: 900px;
    overflow: hidden;
    background: var(--stage);
  }
  .cover {
    position: absolute;
    left: 220px;
    top: 70px;
    width: 760px;
    height: 760px;
    overflow: hidden;
    background: var(--deep-navy);
  }
  .cover__artwork {
    position: absolute;
    inset: 0;
    background:
      radial-gradient(ellipse 55% 10% at 22% 47%, var(--ice) 0%, rgba(120,210,255,0.7) 35%, transparent 75%),
      radial-gradient(ellipse 40% 30% at 60% 48%, rgba(255,255,255,0.45) 0%, transparent 70%),
      radial-gradient(ellipse 60% 55% at 30% 50%, rgba(47,168,240,0.75) 0%, transparent 70%),
      linear-gradient(100deg, var(--deep-navy) 0%, #243a9a 25%, var(--violet) 55%, var(--magenta) 85%, #8a1c5c 100%);
  }
  .cover__artwork::after {
    content: "";
    position: absolute;
    inset: 0;
    background: linear-gradient(180deg, rgba(20,14,50,0.55) 0%, transparent 30%, transparent 65%, rgba(40,20,90,0.7) 100%);
  }
  .cover__title {
    position: absolute;
    left: 236px;
    top: 346px;
    margin: 0;
    font-family: "Arimo", sans-serif;
    font-weight: 400;
    font-size: 27px;
    letter-spacing: 0.2em;
    color: var(--title-ink);
    white-space: nowrap;
  }
  .cover__brand {
    position: absolute;
    left: 0;
    right: 0;
    top: 655px;
    display: flex;
    justify-content: center;
    align-items: center;
    gap: 12px;
    font-family: "Arimo", sans-serif;
    font-weight: 700;
    font-size: 40px;
    letter-spacing: 0.08em;
    color: var(--brand-ink);
  }
  .cover__brand-dot {
    width: 22px;
    height: 22px;
    border-radius: 50%;
    background: var(--brand-ink);
  }
</style>
</head>
<body>
  <main class="cover">
    <div class="cover__artwork" role="img" aria-label="Glowing audio waveform stretching across the cover, blue on the left fading to violet and magenta, with speaker-cone shapes on the right"></div>
    <h1 class="cover__title">BIG ROOM TRACK</h1>
    <div class="cover__brand"><span class="cover__brand-dot"></span>VANTORA</div>
  </main>
</body>
</html>
```